MBRCCUL re-branding website and logo

We are looking for a new webpage design and logo our current page address is www.mbrccul-example.org. We want to create a new design using MBRCCUL Mariners and Bakers Regional Co-operative Credit Union limited and another with the purposed new name MBFC Mariners and Bakers Financial Co-operative, the color scheme is purple and burnt orange. Our new logo and webpage should communicate change and growth purposed theme continuing our legacy here to server past, present and future generations. Our idea for the logo is a live shot of hands of different ages in a circle holding a tree

Target Market(s)

Everyone

Contact Information for Business Card

Company Name
Telephone number
Address
slot to enter employee info

Logo Text

(M & B) Mariners And Bakers Financial Co-operative

Coding

Coded - Design and coding required

Number of Pages Required

2 page

Colors
f37122
fbed22
6b449b

Requirements
Must have
• links for social media

```html
<!DOCTYPE html>
<html lang="en">
<head>
<meta charset="utf-8">
<title>MBFC</title>
<link href="https://fonts.googleapis.com/css2?family=Roboto:wght@300;400;500;700&display=swap" rel="stylesheet">
<style>
:root{
  --purple:#6b449b;
  --purple-dark:#4e2f78;
  --orange:#f37122;
  --yellow:#fbed22;
  --ink:#333338;
  --muted:#777a80;
  --pale:#eef1f6;
  --white:#ffffff;
  --line:#c9bfdc;
}
*{box-sizing:border-box;margin:0;padding:0}
html,body{width:1111px;height:1200px;overflow:hidden;background:var(--white)}
body{font-family:'Roboto',Arial,sans-serif;color:var(--ink)}
.canvas{position:relative;width:1111px;height:1200px;overflow:hidden}
.abs{position:absolute}
a{color:inherit;text-decoration:none}
svg{display:block}

/* ---------- Hero ---------- */
.hero{left:0;top:0;width:550px;height:347px;background:linear-gradient(120deg,#7a55ad 0%,#6b449b 45%,#5a3888 100%)}
.hero-photo{left:0;top:0;width:550px;height:347px;background:radial-gradient(circle at 30% 40%,rgba(255,255,255,.14),transparent 55%),radial-gradient(circle at 75% 60%,rgba(255,255,255,.08),transparent 50%)}
.utility-bar{left:300px;top:0;width:205px;height:19px;background:var(--yellow);display:flex;align-items:center;justify-content:space-around;font-size:6.5px;font-weight:500;color:var(--ink)}
.utility-bar .sign-in{background:var(--purple);color:var(--white);padding:3px 7px}
.brand{left:35px;top:26px;display:flex;align-items:center;gap:6px;color:var(--white);font-size:11px;font-weight:500;letter-spacing:.5px}
.brand-mark{width:14px;height:14px;border-radius:50%;background:var(--white)}
.main-nav{left:170px;top:38px;display:flex;gap:26px;font-size:7px;color:#e6def2;letter-spacing:.2px}
.main-nav .apply{color:var(--yellow);font-weight:500}
.hero-rule{background:rgba(255,255,255,.6);height:1px}
.hero-title{left:48px;top:150px;font-size:18.5px;font-weight:500;color:var(--white)}
.hero-sub{left:48px;top:172px;width:240px;font-size:9.5px;line-height:1.3;color:#e1d8ee;font-weight:300}
.btn-outline-light{left:55px;top:208px;width:100px;height:32px;border:1px solid rgba(255,255,255,.85);color:var(--white);font-size:9px;display:flex;align-items:center;justify-content:center}

.teller{left:353px;top:108px;width:133px;height:236px;background:#f4f4f6;box-shadow:0 2px 8px rgba(0,0,0,.25)}
.teller h3{text-align:center;font-size:10.5px;font-weight:500;color:var(--purple);margin-top:16px}
.teller .tag{text-align:center;font-size:5.5px;color:var(--muted);margin-top:2px}
.teller .field{margin:10px 10px 0;height:22px;border-bottom:1px solid #dcdce2;display:flex;align-items:center;gap:6px;font-size:6px;color:var(--purple)}
.teller .field svg{width:7px;height:7px}
.teller .login-btn{margin:16px auto 0;width:82px;height:24px;background:var(--orange);color:var(--white);font-size:9px;display:flex;align-items:center;justify-content:center}
.teller .links{display:flex;justify-content:space-between;margin:14px 10px 0;font-size:5px;color:var(--muted)}
.teller .phone{display:flex;align-items:center;justify-content:center;gap:6px;margin-top:12px;color:var(--orange);font-size:10px;font-weight:500}

/* ---------- Services ---------- */
.services{left:0;top:347px;width:550px;height:276px;background:var(--pale)}
.service{position:absolute;width:110px;text-align:center;font-size:8px;color:var(--ink)}
.service svg{margin:0 auto 8px;width:24px;height:24px}
.service.active{background:var(--white);box-shadow:0 2px 6px rgba(0,0,0,.12);width:88px;height:90px;padding-top:14px}
.service .apply-link{color:var(--orange);font-size:6.5px;margin-top:8px;text-decoration:underline;font-weight:500}
.btn-outline-purple{border:1px solid var(--purple);color:var(--purple);font-size:8px;display:flex;align-items:center;justify-content:center;background:transparent}

/* ---------- Calculator ---------- */
.calc-section{left:0;top:623px;width:550px;height:254px;background:var(--pale)}
.calc-band{left:238px;top:645px;width:310px;height:188px;background:var(--purple)}
.calc-title{left:38px;top:670px;font-size:18.5px;color:var(--purple);font-weight:400}
.calc-copy{left:46px;top:695px;width:170px;font-size:6.2px;line-height:1.35;color:#55575c}
.pill{position:absolute;height:22px;border:1px solid var(--orange);border-radius:11px;font-size:6.5px;color:var(--purple);display:flex;align-items:center;justify-content:center}
.calc-note{left:262px;top:808px;width:170px;font-size:4.6px;line-height:1.4;color:#e6ddf2}
.calculator{left:345px;top:623px;width:106px;height:166px;background:#e9e9ee;box-shadow:0 2px 8px rgba(0,0,0,.25)}
.calc-display{height:52px;background:#f7f7f9;text-align:right;padding:5px 6px}
.calc-display .expr{font-size:7.5px;color:var(--ink)}
.calc-display .result{font-size:15px;color:var(--orange);margin-top:8px}
.calc-keys{display:grid;grid-template-columns:repeat(4,1fr);row-gap:10px;padding:9px 4px 0;font-size:8.5px;color:var(--purple);text-align:center}
.calc-keys .eq{background:var(--white)}

/* ---------- Membership ---------- */
.member-photo{left:145px;top:877px;width:403px;height:150px;background:linear-gradient(90deg,#e88a4a 0%,#f3a06a 45%,#e7853f 100%)}
.member-box{left:48px;top:897px;width:133px;height:116px;background:var(--purple);color:var(--white);padding:10px 12px}
.member-box h3{font-size:13.5px;font-weight:500;line-height:1.1}
.member-box p{font-size:7.5px;line-height:1.25;margin-top:3px;color:#ece4f7}
.member-box .btn{margin-top:10px;width:100px;height:26px;border:1px solid var(--white);font-size:8px;display:flex;align-items:center;justify-content:center}

/* ---------- Rates ---------- */
.section-title{position:absolute;font-size:18.5px;font-weight:300;color:var(--ink);text-align:center}
.rate{position:absolute;width:110px;text-align:center}
.rate svg{margin:0 auto 6px;width:28px;height:26px}
.rate .name{color:var(--orange);font-size:10.5px;font-weight:500}
.rate .low{color:var(--muted);font-size:7.5px}
.rate .apr{color:var(--purple);font-size:10px;font-weight:500}

/* ---------- Members carousel ---------- */
.member-card{position:absolute;width:78px;height:125px}
.member-card .frame{position:absolute;right:-7px;top:-7px;width:38px;height:38px;background:var(--purple)}
.member-card .body{position:absolute;left:0;top:0;width:78px;height:125px;background:var(--white);box-shadow:0 1px 4px rgba(0,0,0,.2);padding:4px}
.member-card .photo{width:70px;height:74px}
.member-card p{font-size:4.6px;line-height:1.35;color:#666;margin-top:4px}
.member-card .more{position:absolute;right:6px;bottom:6px;background:var(--orange);color:var(--white);font-size:3.8px;padding:2px 4px}
.arrow{position:absolute;width:22px;height:22px;background:var(--orange);display:flex;align-items:center;justify-content:center}

/* ---------- News ---------- */
.news{position:absolute;width:136px}
.news .date{font-size:5.5px;color:var(--muted);margin-left:8px}
.news .photo{margin-top:4px;width:136px;height:48px}
.news h4{font-size:8.5px;font-weight:400;line-height:1.2;color:var(--ink);margin-top:4px}
.news .read{position:absolute;right:0;top:86px;width:58px;height:21px;background:var(--purple);color:var(--white);font-size:5.5px;display:flex;align-items:center;justify-content:center}

/* ---------- Join ---------- */
.join-bg{left:562px;top:699px;width:549px;height:283px;background:var(--pale)}
.join-frame{left:672px;top:750px;width:341px;height:126px;background:var(--purple)}
.join-photo{left:639px;top:774px;width:341px;height:165px;background:linear-gradient(110deg,#f5ea3a 0%,#fbed22 50%,#f2e21c 100%)}
.join-title{left:602px;top:786px;font-size:22.5px;font-weight:700;color:var(--orange)}
.join-input{left:678px;top:851px;width:189px;height:25px;background:var(--white)}
.join-btn{left:867px;top:851px;width:92px;height:25px;background:var(--purple);color:var(--white);font-size:6.5px;display:flex;align-items:center;justify-content:center}
.join-copy{left:660px;top:889px;width:300px;font-size:9px;line-height:1.3;color:var(--ink)}
.to-top{left:1036px;top:972px;width:24px;height:24px;background:var(--orange);display:flex;align-items:center;justify-content:center}

/* ---------- Footer ---------- */
.footer-col{position:absolute;top:1031px}
.footer-col h5{font-size:5.5px;font-weight:700;color:var(--purple);letter-spacing:.3px;margin-bottom:14px}
.footer-col li{list-style:none;font-size:5.3px;color:var(--purple);line-height:12px}
.zip{left:968px;top:1057px;width:56px;height:26px;background:var(--pale);font-size:5px;color:var(--muted);display:flex;align-items:center;padding-left:8px}
.zip-btn{left:1024px;top:1057px;width:34px;height:26px;background:var(--orange);color:var(--white);font-size:5.5px;display:flex;align-items:center;justify-content:center}
.footer-phone{left:620px;top:1147px;display:flex;align-items:center;gap:6px;font-size:8px;font-weight:500;color:var(--purple)}
.copyright{left:713px;top:1155px;font-size:4.8px;color:var(--muted)}
.social{left:1013px;top:1152px;display:flex;align-items:center;gap:3px;font-size:6px;font-weight:500;color:var(--purple)}
.social .sq{width:11px;height:11px;background:var(--purple)}
.social .sq.alt{background:var(--orange)}
.rule{position:absolute;height:1px;background:var(--line)}
</style>
</head>
<body>
<div class="canvas">

  <!-- Hero -->
  <section class="abs hero">
    <div class="abs hero-photo" role="img" aria-label="Photo of smiling members in an office, tinted purple"></div>
    <div class="abs utility-bar">
      <a href="#">Become A Member</a><a href="#">Contact us</a><a href="#">Locations</a><a class="sign-in" href="#">Sign In</a>
    </div>
    <div class="abs brand"><span class="brand-mark"></span><span>MBFC</span></div>
    <nav class="abs main-nav">
      <a href="#">MY CREDIT UNION</a><a href="#">PRODUCTS &amp; SERVICES</a><a href="#">TOOLS &amp; BENEFITS</a><a class="apply" href="#">APPLY FOR LOAN</a>
    </nav>
    <div class="abs hero-rule" style="left:38px;top:137px;width:52px"></div>
    <h1 class="abs hero-title">Lorem ipsum dolor sit amet</h1>
    <p class="abs hero-sub">consectetur adipiscing elit, sed do eiusmod tempor incididunt ut labore et dolore magna aliqua.</p>
    <div class="abs hero-rule" style="left:272px;top:203px;width:16px"></div>
    <a class="abs btn-outline-light" href="#">Join Now</a>

    <div class="abs teller">
      <h3>Teller Login</h3>
      <p class="tag">Your Personal Online Teller</p>
      <div class="field"><svg viewBox="0 0 10 10"><circle cx="5" cy="3" r="2.2" fill="none" stroke="#6b449b"/><path d="M1 10c0-3 8-3 8 0" fill="none" stroke="#6b449b"/></svg>Username</div>
      <div class="field"><svg viewBox="0 0 10 10"><rect x="1.5" y="4.5" width="7" height="5" fill="none" stroke="#6b449b"/><path d="M3 4.5V3a2 2 0 0 1 4 0v1.5" fill="none" stroke="#6b449b"/></svg>Password</div>
      <a class="login-btn" href="#">LOGIN</a>
      <div class="links"><span>Forgot Password</span><span>Sign Up</span></div>
      <div class="phone"><svg width="9" height="14" viewBox="0 0 9 14"><rect x="0.5" y="0.5" width="8" height="13" rx="1.5" fill="none" stroke="#f37122"/><line x1="3" y1="11.5" x2="6" y2="11.5" stroke="#f37122"/></svg>1-800-555-0179</div>
    </div>
  </section>

  <!-- Services -->
  <section class="abs services">
    <div class="service" style="left:90px;top:30px">
      <svg viewBox="0 0 24 24" fill="none" stroke="#6b449b" stroke-width="1.3"><path d="M3 12a9 9 0 0 1 18 0z"/><path d="M12 12v7a2 2 0 0 1-4 0" stroke="#f37122"/><path d="M12 3v-1"/></svg>
      Mortgage Loan</div>
    <div class="service active" style="left:232px;top:25px">
      <svg viewBox="0 0 24 24" fill="none" stroke="#f37122" stroke-width="1.3"><ellipse cx="9" cy="6" rx="5" ry="2"/><path d="M4 6v10c0 1.1 2.2 2 5 2s5-.9 5-2V6"/><path d="M4 10c0 1.1 2.2 2 5 2s5-.9 5-2M4 14c0 1.1 2.2 2 5 2s5-.9 5-2" stroke="#6b449b"/><ellipse cx="17" cy="12" rx="4" ry="1.6"/><path d="M13 12v7c0 .9 1.8 1.6 4 1.6s4-.7 4-1.6v-7"/></svg>
      Consumer Loans<div class="apply-link">APPLY</div></div>
    <div class="service" style="left:355px;top:30px">
      <svg viewBox="0 0 24 24" fill="none" stroke="#f37122" stroke-width="1.3"><rect x="3" y="4" width="18" height="15" rx="1"/><circle cx="12" cy="11.5" r="3.5" stroke="#6b449b"/><path d="M6 19v2M18 19v2"/></svg>
      Safety Deposit Box</div>
    <div class="service" style="left:90px;top:135px">
      <svg viewBox="0 0 24 24" fill="none" stroke="#f37122" stroke-width="1.3"><rect x="3" y="6" width="18" height="12" rx="1.5"/><line x1="3" y1="10" x2="21" y2="10" stroke="#6b449b"/></svg>
      Card Services</div>
    <div class="service" style="left:220px;top:135px">
      <svg viewBox="0 0 24 24" fill="none" stroke="#6b449b" stroke-width="1.3"><rect x="3" y="6" width="18" height="13" rx="1.5"/><rect x="14" y="10" width="7" height="5" stroke="#f37122"/></svg>
      Loans on the Go</div>
    <div class="service" style="left:355px;top:135px">
      <svg viewBox="0 0 24 24" fill="none" stroke="#f37122" stroke-width="1.3"><circle cx="12" cy="8" r="4"/><path d="M5 21c0-4 3-7 7-7s7 3 7 7" stroke="#6b449b"/><path d="M12 14l-2 4h4z"/></svg>
      Professional Loans</div>
    <a class="abs btn-outline-purple" href="#" style="left:220px;top:216px;width:116px;height:36px">View All Services</a>
  </section>

  <!-- Financial calculator -->
  <section class="abs calc-section"></section>
  <div class="abs calc-band"></div>
  <div class="rule" style="left:25px;top:650px;width:58px;background:var(--purple)"></div>
  <div class="rule" style="left:100px;top:650px;width:8px;background:var(--purple)"></div>
  <h2 class="abs calc-title">Financial Calculator</h2>
  <p class="abs calc-copy">sed quia consequuntur magni dolores eos qui ratione voluptatem sequi nesciunt. Neque porro quisquam est, qui dolorem ipsum quia dolor sit amet, consectetur, adipisci velit.</p>
  <a class="pill" href="#" style="left:34px;top:742px;width:84px">Savings Calculators</a>
  <a class="pill" href="#" style="left:134px;top:742px;width:83px">Auto Calculators</a>
  <a class="pill" href="#" style="left:34px;top:777px;width:84px">Loan Calculators</a>
  <a class="pill" href="#" style="left:134px;top:777px;width:83px">Mortgage Calculators</a>
  <div class="rule" style="left:202px;top:826px;width:22px;background:var(--purple)"></div>
  <p class="abs calc-note">*sed quia consequuntur magni dolores eos qui ratione voluptatem sequi nesciunt. Neque porro quisquam est, qui dolorem ipsum quia dolor sit amet, consectetur, adipisci velit.</p>
  <div class="abs calculator">
    <div class="calc-display"><div class="expr">46.39 x 12</div><div class="result">556.68</div></div>
    <div class="calc-keys">
      <span>C</span><span>+/-</span><span>%</span><span>÷</span>
      <span>7</span><span>8</span><span>9</span><span>x</span>
      <span>4</span><span>5</span><span>6</span><span>+</span>
      <span>1</span><span>2</span><span>3</span><span>−</span>
      <span>0</span><span>·</span><span>◀</span><span class="eq">=</span>
    </div>
  </div>

  <!-- Membership benefits -->
  <div class="abs member-photo" role="img" aria-label="Photos of a group of staff and a member shopping online, tinted orange"></div>
  <div class="rule" style="left:60px;top:892px;width:14px;background:var(--white)"></div>
  <div class="abs member-box">
    <h3>Membership<br>Benefits</h3>
    <p>Learn More About<br>the Endless Benefits</p>
    <a class="btn" href="#">See Details</a>
  </div>

  <!-- Featured rates, left column -->
  <div class="rule" style="left:48px;top:1051px;width:135px"></div>
  <div class="rule" style="left:245px;top:1051px;width:22px"></div>
  <h2 class="section-title" style="left:0;top:1063px;width:550px">Featured Rates</h2>
  <div class="rate" style="left:74px;top:1110px">
    <svg viewBox="0 0 28 26" fill="none" stroke="#6b449b" stroke-width="1.3"><path d="M4 18l2-6h16l2 6z"/><rect x="3" y="18" width="22" height="4"/><circle cx="8" cy="22" r="2" fill="#f37122" stroke="none"/><circle cx="20" cy="22" r="2" fill="#f37122" stroke="none"/><circle cx="14" cy="6" r="4" stroke="#f37122"/></svg>
    <div class="name">Auto Loan</div><div class="low">as low as</div><div class="apr">7.00% Apr*</div></div>
  <div class="rate" style="left:220px;top:1110px">
    <svg viewBox="0 0 28 26" fill="none" stroke="#6b449b" stroke-width="1.3"><circle cx="14" cy="13" r="6" fill="#f37122" stroke="none"/><path d="M3 20c4-2 7 2 11 1s7-3 11-2"/><path d="M8 5l2-2M20 5l-2-2"/></svg>
    <div class="name">Consumer Loans</div><div class="low">as low as</div><div class="apr">9.00% Apr*</div></div>
  <div class="rate" style="left:358px;top:1110px">
    <svg viewBox="0 0 28 26" fill="none" stroke="#6b449b" stroke-width="1.3"><path d="M5 12L14 4l9 8"/><rect x="8" y="11" width="12" height="8" fill="#f37122" stroke="none"/><path d="M3 22c4-2 7 1 11 0s7-2 11-1"/></svg>
    <div class="name">Mortgages</div><div class="low">as low as</div><div class="apr">8.25% Apr*</div></div>

  <!-- Featured rates, right column -->
  <h2 class="section-title" style="left:560px;top:0;width:551px">Featured Rates</h2>
  <div class="rate" style="left:636px;top:45px">
    <svg viewBox="0 0 28 26" fill="none" stroke="#6b449b" stroke-width="1.3"><path d="M4 18l2-6h16l2 6z"/><rect x="3" y="18" width="22" height="4"/><circle cx="8" cy="22" r="2" fill="#f37122" stroke="none"/><circle cx="20" cy="22" r="2" fill="#f37122" stroke="none"/><circle cx="14" cy="6" r="4" stroke="#f37122"/></svg>
    <div class="name">Auto Loan</div><div class="low">as low as</div><div class="apr">7.00% Apr*</div></div>
  <div class="rate" style="left:785px;top:45px">
    <svg viewBox="0 0 28 26" fill="none" stroke="#6b449b" stroke-width="1.3"><circle cx="14" cy="13" r="6" fill="#f37122" stroke="none"/><path d="M3 20c4-2 7 2 11 1s7-3 11-2"/><path d="M8 5l2-2M20 5l-2-2"/></svg>
    <div class="name">Consumer Loans</div><div class="low">as low as</div><div class="apr">9.00% Apr*</div></div>
  <div class="rate" style="left:935px;top:45px">
    <svg viewBox="0 0 28 26" fill="none" stroke="#6b449b" stroke-width="1.3"><path d="M5 12L14 4l9 8"/><rect x="8" y="11" width="12" height="8" fill="#f37122" stroke="none"/><path d="M3 22c4-2 7 1 11 0s7-2 11-1"/></svg>
    <div class="name">Mortgages</div><div class="low">as low as</div><div class="apr">8.25% Apr*</div></div>
  <a class="abs btn-outline-purple" href="#" style="left:782px;top:148px;width:114px;height:36px">Apply For Loan Now!</a>
  <div class="rule" style="left:865px;top:187px;width:120px"></div>
  <div class="abs" style="left:1003px;top:193px;font-size:4.6px;color:var(--muted)">*APR - Annual Percentage Rate</div>
  <div class="rule" style="left:1030px;top:202px;width:52px"></div>

  <!-- Our members -->
  <h2 class="section-title" style="left:560px;top:217px;width:551px">Our Members</h2>
  <div class="arrow" style="left:572px;top:287px"><svg width="6" height="8" viewBox="0 0 6 8"><path d="M5 0L1 4l4 4" fill="none" stroke="#fff" stroke-width="1.4"/></svg></div>
  <div class="arrow" style="left:1074px;top:348px"><svg width="6" height="8" viewBox="0 0 6 8"><path d="M1 0l4 4-4 4" fill="none" stroke="#fff" stroke-width="1.4"/></svg></div>

  <div class="member-card" style="left:610px;top:272px"><div class="frame"></div><div class="body"><div class="photo" role="img" aria-label="Portrait of a member" style="background:linear-gradient(135deg,#5c6a5e,#3b4046)"></div><p>Ut enim ad minima veniam, quis nostrum exercitationem ullam corporis suscipit</p><span class="more">Read More</span></div></div>
  <div class="member-card" style="left:736px;top:272px"><div class="frame"></div><div class="body"><div class="photo" role="img" aria-label="Portrait of a member" style="background:linear-gradient(135deg,#e8e0a8,#d8b98a)"></div><p>Ut enim ad minima veniam, quis nostrum exercitationem ullam corporis suscipit</p><span class="more">Read More</span></div></div>
  <div class="member-card" style="left:861px;top:272px"><div class="frame"></div><div class="body"><div class="photo" role="img" aria-label="Portrait of a member" style="background:linear-gradient(135deg,#f1ece6,#c9a98c)"></div><p>Ut enim ad minima veniam, quis nostrum exercitationem ullam corporis suscipit</p><span class="more">Read More</span></div></div>
  <div class="member-card" style="left:986px;top:272px"><div class="frame"></div><div class="body"><div class="photo" role="img" aria-label="Portrait of a couple of members" style="background:linear-gradient(135deg,#b8c6a8,#d49a7e)"></div><p>Ut enim ad minima veniam, quis nostrum exercitationem ullam corporis suscipit</p><span class="more">Read More</span></div></div>

  <!-- News -->
  <h2 class="section-title" style="left:560px;top:464px;width:551px">News &amp; Updates</h2>
  <div class="rule" style="left:590px;top:497px;width:132px"></div>
  <div class="rule" style="left:740px;top:497px;width:38px"></div>

  <article class="news" style="left:586px;top:510px"><div class="date">February 16, 2017</div><div class="photo" role="img" aria-label="Photo of a toy car on stacks of coins" style="background:linear-gradient(180deg,#f1eee8,#c9a46a)"></div><h4>At vero eos et accusamus et iusto odio dignissimos</h4><a class="read" href="#">Read Full Story</a></article>
  <article class="news" style="left:765px;top:510px"><div class="date">February 26, 2017</div><div class="photo" role="img" aria-label="Photo of a model house on documents" style="background:linear-gradient(180deg,#dfe5ec,#8e9aab)"></div><h4>At vero eos et accusamus et iusto odio dignissimos</h4><a class="read" href="#">Read Full Story</a></article>
  <article class="news" style="left:944px;top:510px"><div class="date">March 26, 2017</div><div class="photo" role="img" aria-label="Photo of a family talking with an advisor" style="background:linear-gradient(180deg,#efe6dc,#c79b78)"></div><h4>At vero eos et accusamus et iusto odio dignissimos</h4><a class="read" href="#">Read Full Story</a></article>
  <div class="rule" style="left:1028px;top:637px;width:22px"></div>
  <div class="rule" style="left:1060px;top:637px;width:22px"></div>
  <a class="abs btn-outline-purple" href="#" style="left:782px;top:646px;width:114px;height:36px">View All</a>

  <!-- Join -->
  <section class="abs join-bg"></section>
  <div class="abs join-frame"></div>
  <div class="abs join-photo" role="img" aria-label="Photo of a smiling couple, tinted yellow"></div>
  <h2 class="abs join-title">Join Us Today</h2>
  <div class="abs join-input"></div>
  <a class="abs join-btn" href="#">Become a Member</a>
  <p class="abs join-copy">Excepteur sint occaecat cupidatat non proident, sunt in culpa qui officia deserunt mollit anim id est laborum."</p>
  <a class="abs to-top" href="#"><svg width="8" height="6" viewBox="0 0 8 6"><path d="M0 5l4-4 4 4" fill="none" stroke="#fff" stroke-width="1.4"/></svg></a>

  <!-- Footer -->
  <div class="footer-col" style="left:638px"><h5>PERSONAL</h5><ul><li>Bank</li><li>Credit Cards</li><li>Loans</li><li>Insurance</li><li>Investing</li></ul></div>
  <div class="footer-col" style="left:702px"><h5>BUSINESS</h5><ul><li>Bank</li><li>Credit Cards</li><li>Loans</li><li>Insurance</li></ul></div>
  <div class="footer-col" style="left:763px"><h5>BECOME A MEMBER</h5><ul><li>Why Credit Union?</li><li>Sign Up</li><li>Compare Rates</li><li>Members Only Offers</li></ul></div>
  <div class="footer-col" style="left:855px"><h5>HELPFUL LINKS</h5><ul><li>Why Credit Union?</li><li>Sign Up</li><li>Compare Rates</li><li>Members Only Offers</li></ul></div>
  <div class="footer-col" style="left:1002px"><h5>LOCATE A BRANCH</h5></div>
  <div class="abs zip">ZIP CODE</div>
  <a class="abs zip-btn" href="#">Submit</a>

  <div class="abs footer-phone"><svg width="12" height="20" viewBox="0 0 12 20"><rect x="0.7" y="0.7" width="10.6" height="18.6" rx="2" fill="none" stroke="#6b449b" stroke-width="1.2"/><line x1="4" y1="16" x2="8" y2="16" stroke="#6b449b"/></svg>1-800-555-0145</div>
  <div class="abs copyright">© 2017 MBFC. All Rights Reserved.</div>
  <div class="abs social">Get Social <span class="sq alt"></span><span class="sq"></span></div>

</div>
</body>
</html>
```